Commercial Swimming Pool - Design-Build Contractor Website Design

I need a new website that will feature our newly developed logo and trade name as well as provide a fully updated site experience. We are not a residential builder - we strictly design and install high-end commercial pools. I need the website to highlight our portfolio and communicate the various types of projects in which we specialize. I want the effect of the site to reflect the high-end nature of our services - projects like the 57th floor spa at the Phila Tall Cedars, the aquatic therapy portion of the Phila Quillers training facility, a 5om indoor competition pool for the prestigious Draymoor Academy, the indoor water park at The Brackwell Lodge or the recent country club renovation projects we've completed in our region (to name a few examples).

```html
<!DOCTYPE html>
<html lang="en">
<head>
<meta charset="utf-8">
<title>Calder Aquatics — Commercial Pools</title>
<link href="https://fonts.googleapis.com/css2?family=Jost:wght@300;400;500&family=Noto+Serif:wght@400;700&display=swap" rel="stylesheet">
<style>
:root{
  --navy:#1b2550;
  --sky:#3fb3e0;
  --page:#f5f7f5;
  --band:#dcf2f3;
  --grey:#7a7f8c;
  --line:#c9cdd4;
  --soft:#aeb4c0;
}
*{margin:0;padding:0;box-sizing:border-box}
html,body{width:1200px;height:3750px;overflow:hidden}
body{background:var(--page);position:relative;font-family:"Noto Serif",serif;color:var(--navy)}
.abs{position:absolute}
.sans{font-family:"Jost",sans-serif}
.center{transform:translateX(-50%);text-align:center;white-space:nowrap}

/* nav */
.nav a{position:absolute;top:31px;font:400 13px "Jost",sans-serif;color:#3a4160;text-decoration:none;transform:translateX(-50%)}
.brand-mark{left:600px;top:20px;transform:translateX(-50%);font:500 34px "Jost",sans-serif;color:var(--navy);letter-spacing:1px}

/* hero */
.hero{left:0;top:79px;width:1200px;height:501px;
  background:linear-gradient(180deg,#f6f2e9 0%,#f3ece0 30%,#e8d7bf 42%,#cfeff0 55%,#9fdde3 75%,#8fd5df 100%)}
.hero-title{left:600px;top:166px;font:400 58px/1 "Jost",sans-serif;color:var(--sky)}
.hero-sub{left:600px;top:220px;font:400 44px/1 "Jost",sans-serif;color:var(--navy)}
.pillar{top:318px;font:300 29px "Jost",sans-serif;color:#5b6170;letter-spacing:.5px}
.btn{position:absolute;display:flex;align-items:center;justify-content:center;font:400 16px "Jost",sans-serif;text-decoration:none}
.btn-dark{border:2px solid var(--navy);color:var(--navy)}
.btn-sky{border:1.5px solid var(--sky);color:var(--sky)}
.dots span{position:absolute;top:459px;width:11px;height:11px;border-radius:50%;background:#8f9ea3}
.dots span.on{background:var(--navy)}

/* headings */
.h-section{font:400 34px/1 "Jost",sans-serif;color:var(--navy);letter-spacing:.5px}
.reflect{font:400 34px/1 "Jost",sans-serif;color:var(--navy);opacity:.18;transform:translateX(-50%) scaleY(-.45);transform-origin:top}
.lead{font-size:15.5px;line-height:23px;color:#4a5068;text-align:center}

/* process */
.step{top:848px;font:400 13px "Jost",sans-serif;color:var(--soft);letter-spacing:.5px}
.step.on{color:var(--sky)}
.step-note{left:600px;top:912px;width:150px;transform:translateX(-50%);font-size:11.5px;line-height:16px;color:var(--grey);text-align:center}

/* services */
.band{left:0;width:1200px;background:var(--band)}
.photo{position:absolute}
.card-title{font:400 20px "Jost",sans-serif;color:var(--navy)}
.card-text{width:175px;font-size:11.5px;line-height:16px;color:#555b70}

/* portfolio */
.proj-title{font:400 19px "Jost",sans-serif;color:var(--navy);white-space:nowrap}
.meta{font-size:10px;line-height:16px;color:#555b70}
.meta b{color:var(--navy)}
.proj-text{width:340px;font-size:11px;line-height:16px;color:#8b909d}
.more{font:500 12px "Jost",sans-serif;color:var(--sky)}
.rule{height:1px;background:var(--line)}

/* testimonial */
.quote-text{width:355px;font-size:13px;line-height:19px;color:#8b909d}
.quote-name{font:700 13px "Noto Serif",serif;color:var(--sky)}
.quote-role{font:400 10px "Jost",sans-serif;color:var(--navy)}

/* footer */
.cta{font:400 31px "Jost",sans-serif;color:var(--navy)}
.foot-logo{font:400 30px/1 "Jost",sans-serif;color:var(--sky)}
.contact{right:270px;text-align:right;font:400 13.5px/21px "Jost",sans-serif;color:var(--navy)}
.social span{position:absolute;top:3590px;width:22px;height:22px;border-radius:50%;background:var(--navy)}
.foot-nav a{position:absolute;top:3650px;transform:translateX(-50%);font:400 13px "Jost",sans-serif;color:#3a4160;text-decoration:none}
.url{left:600px;top:3722px;font:400 12px "Jost",sans-serif;color:#3a4160}
</style>
</head>
<body>

<!-- navigation -->
<nav class="nav">
  <a href="#" style="left:389px">Services</a>
  <a href="#" style="left:488px">Portfolio</a>
  <a href="#" style="left:705px">Gallery</a>
  <a href="#" style="left:808px">Get In Touch</a>
</nav>
<div class="abs brand-mark">Calder</div>

<!-- hero -->
<section class="abs hero" role="img" aria-label="Bright indoor pool hall with white roof structure and turquoise water"></section>
<div class="abs hero-title center">CALDER</div>
<div class="abs hero-sub center">AQUATICS</div>
<div class="abs pillar center" style="left:316px">DESIGN</div>
<div class="abs pillar center" style="left:600px">CONSTRUCTION</div>
<div class="abs pillar center" style="left:878px">EXCELLENCE</div>
<a class="btn btn-dark" href="#" style="left:508px;top:470px;width:182px;height:45px">GET IN TOUCH</a>
<div class="dots"><span class="on" style="left:563px"></span><span style="left:594px"></span><span style="left:625px"></span></div>

<!-- intro -->
<h1 class="abs h-section center" style="left:600px;top:628px">WE DESIGN AND BUILD COMMERCIAL POOLS</h1>
<div class="abs reflect" style="left:600px;top:666px;white-space:nowrap">WE DESIGN AND BUILD COMMERCIAL POOLS</div>
<p class="abs lead center" style="left:600px;top:690px;white-space:normal;width:500px">We are a firm focused on designing and installing high-end commercial pools for companies and facilities. We bring unparalleled expertise to serve esteemed commercial clientele.</p>

<h2 class="abs sans center" style="left:600px;top:794px;font-weight:400;font-size:23px">Our Unique Process</h2>
<div class="abs step center" style="left:446px">1. SURVEY</div>
<div class="abs step on center" style="left:600px">2. DESIGN</div>
<div class="abs step center" style="left:748px">3. INSTALLATION</div>
<svg class="abs" style="left:440px;top:870px" width="320" height="30" viewBox="0 0 320 30">
  <line x1="11" y1="15" x2="308" y2="15" stroke="#6d7590" stroke-width="3"/>
  <circle cx="11" cy="15" r="5" fill="#5a6280"/>
  <circle cx="308" cy="15" r="5" fill="#5a6280"/>
  <circle cx="160" cy="15" r="13" fill="#eef0f3" stroke="#c9cdd6" stroke-width="3"/>
  <circle cx="160" cy="15" r="6" fill="var(--navy)"/>
</svg>
<p class="abs step-note">At the designing phase we plan out the design of the pool according to the requirements and client specifications.</p>

<!-- services -->
<div class="abs band" style="top:1159px;height:571px"></div>
<div class="photo" style="left:231px;top:1072px;width:238px;height:343px;background:linear-gradient(180deg,#e8eef2 0%,#cfd9e2 45%,#4b86c4 65%,#1d4f9a 100%)" role="img" aria-label="Indoor competition pool under a glass roof with pennant flags"></div>
<div class="photo" style="left:481px;top:1140px;width:238px;height:342px;background:linear-gradient(180deg,#3b3b44 0%,#b07a5e 28%,#5a4a4c 45%,#1b1b22 70%,#070709 100%)" role="img" aria-label="Outdoor pool at dusk with steps into dark water"></div>
<div class="photo" style="left:731px;top:1072px;width:238px;height:343px;background:linear-gradient(135deg,#3e4a4c 0%,#7a4b35 35%,#d8d8d4 55%,#5bc6c9 75%,#3a3638 100%)" role="img" aria-label="Unique spa pool with wooden wall and lounge seating"></div>

<h3 class="abs card-title" style="left:229px;top:1428px">INDOOR POOLS</h3>
<p class="abs card-text" style="left:231px;top:1463px">Sed eiusmod tempor incididunt ut labore et dolore magna aliqua. Lorem ipsum dolor sit amet, elitm</p>
<h3 class="abs card-title" style="left:479px;top:1496px">OUTDOOR POOLS</h3>
<p class="abs card-text" style="left:479px;top:1527px">Lorem ipsum dolor sit amet, consectetur adipiscing elit, sed do eiusmod tempor incididunt ut labore et dolore magna</p>
<h3 class="abs card-title" style="left:729px;top:1428px">UNIQUE POOLS</h3>
<p class="abs card-text" style="left:731px;top:1463px">Manga aqulia consectetur adipiscing elit, sed do eiusmod tempor incididunt ut labore et dolore magna aliqua.</p>
<a class="btn btn-sky" href="#" style="left:508px;top:1645px;width:182px;height:44px">GET IN TOUCH</a>

<!-- portfolio -->
<h2 class="abs h-section center" style="left:600px;top:1796px">PORTFOLIO</h2>
<div class="abs reflect" style="left:600px;top:1832px">PORTFOLIO</div>
<p class="abs sans center" style="left:600px;top:1845px;font-size:15px;line-height:23px;white-space:normal;width:360px">Check out our extensive list of past projects for inspiration and immaculate track record</p>

<article>
  <div class="photo" style="left:231px;top:1954px;width:249px;height:249px;background:linear-gradient(180deg,#3a3430 0%,#d7d0c8 35%,#8fb8c7 60%,#bcb5ae 100%)" role="img" aria-label="Sky-level spa pool with curved lounge chairs"></div>
  <h3 class="abs proj-title" style="left:518px;top:2023px">57th Floor Spa, The Tall Cedars</h3>
  <p class="abs meta" style="left:518px;top:2058px"><b>Client:</b> Tall Cedars Spa<br><b>Completion Date:</b> January 2019</p>
  <p class="abs proj-text" style="left:518px;top:2106px">Lorem ipsum dolor sit amet, consectetur adipiscing elit, sed do eiusmod tempor incididunt ut labore et dolore magna aliqua.</p>
  <a class="abs more" style="left:518px;top:2175px">Learn more</a>
  <div class="abs rule" style="left:480px;top:2203px;width:488px"></div>
</article>

<article>
  <div class="photo" style="left:231px;top:2242px;width:249px;height:249px;background:linear-gradient(180deg,#a8d8ea 0%,#3d9fd6 40%,#1b6fc0 75%,#2a86cc 100%)" role="img" aria-label="Swimmer underwater in a bright blue therapy pool"></div>
  <h3 class="abs proj-title" style="left:518px;top:2311px">Aquatic therapy pool, Phila Quillers Training Facility</h3>
  <p class="abs meta" style="left:518px;top:2346px"><b>Client:</b> Philadelphia Quillers<br><b>Completion Date:</b> December 2017</p>
  <p class="abs proj-text" style="left:518px;top:2394px">Consectetur adipiscing elit, sed do eiusmod tempor incididunt ut labore et dolore magna aliqua. Lorem ipsum dolor sit amet.</p>
  <a class="abs more" style="left:518px;top:2463px">Learn more</a>
  <div class="abs rule" style="left:480px;top:2491px;width:488px"></div>
</article>

<article>
  <div class="photo" style="left:231px;top:2529px;width:249px;height:249px;background:linear-gradient(180deg,#dfe4ea 0%,#b9c4d2 30%,#2c4fa8 60%,#4aa2c8 100%)" role="img" aria-label="Indoor competition pool with lane ropes and flags"></div>
  <h3 class="abs proj-title" style="left:518px;top:2598px">Aquatic Center, Draymoor Academy</h3>
  <p class="abs meta" style="left:518px;top:2633px"><b>Client:</b> Draymoor Academy<br><b>Completion Date:</b> July 2022</p>
  <p class="abs proj-text" style="left:518px;top:2681px">Amet sit, consectetur adipiscing elit, sed do eiusmod tempor incididunt ut labore et dolore magna aliqua.</p>
  <a class="abs more" style="left:518px;top:2750px">Learn more</a>
  <div class="abs rule" style="left:480px;top:2778px;width:488px"></div>
</article>

<svg class="abs" style="left:580px;top:2805px" width="40" height="40" viewBox="0 0 40 40">
  <circle cx="20" cy="20" r="18" fill="none" stroke="var(--sky)" stroke-width="1.5"/>
  <line x1="20" y1="11" x2="20" y2="29" stroke="var(--sky)" stroke-width="1.5"/>
  <line x1="11" y1="20" x2="29" y2="20" stroke="var(--sky)" stroke-width="1.5"/>
</svg>
<div class="abs more center" style="left:600px;top:2850px;font-size:14px;font-weight:400">View More</div>

<!-- testimonial -->
<h2 class="abs h-section center" style="left:600px;top:2962px;font-size:26px">WHAT OUR CUSTOMERS SAY</h2>
<div class="abs reflect" style="left:600px;top:2991px;font-size:26px;white-space:nowrap">WHAT OUR CUSTOMERS SAY</div>

<div class="abs" style="left:281px;top:3095px;width:70px;height:70px;border-radius:50%;border:4px solid var(--sky);background:linear-gradient(135deg,#d9dde2,#5d636b)" role="img" aria-label="Portrait of the client"></div>
<svg class="abs" style="left:380px;top:3060px" width="30" height="200" viewBox="0 0 30 200">
  <line x1="15" y1="5" x2="15" y2="195" stroke="#6d7590" stroke-width="3"/>
  <circle cx="15" cy="5" r="5" fill="#5a6280"/>
  <circle cx="15" cy="70" r="12" fill="#eef0f3" stroke="#c9cdd6" stroke-width="3"/>
  <circle cx="15" cy="70" r="6" fill="var(--navy)"/>
  <circle cx="15" cy="133" r="5" fill="#5a6280"/>
  <circle cx="15" cy="194" r="5" fill="#5a6280"/>
</svg>
<div class="abs sans" style="left:447px;top:3100px;font-size:34px;color:var(--sky);line-height:1">&ldquo;</div>
<p class="abs quote-text" style="left:482px;top:3120px">Lorem ipsum dolor sit amet, consectetur adipiscing elit, sed do eiusmod tempor incididunt ut labore et dolore magna aliqua. Quis ipsum suspendisse ultrices gravida. Risus commodo viverra maecenas accumsan lacus vel facilisis.</p>
<div class="abs quote-name" style="left:485px;top:3214px">Martin Ellery</div>
<div class="abs quote-role" style="left:508px;top:3236px">- Harbor Spa CEO</div>

<!-- footer -->
<footer class="abs band" style="top:3358px;height:392px"></footer>
<h2 class="abs cta" style="left:266px;top:3422px">LET’S WORK TOGETHER</h2>
<a class="btn btn-sky" href="#" style="left:748px;top:3422px;width:182px;height:44px">GET IN TOUCH</a>

<div class="abs foot-logo" style="left:268px;top:3524px">CALDER</div>
<div class="abs sans" style="left:268px;top:3554px;font-size:20px;color:var(--navy);line-height:1">AQUATICS</div>

<address class="abs contact" style="top:3520px;font-style:normal">(245) 555 0140<br>info@calderaquatics.com<br>Bl 2. 48th Ave. Lakeport</address>
<div class="social"><span style="left:845px"></span><span style="left:877px"></span><span style="left:909px"></span></div>

<nav class="foot-nav">
  <a href="#" style="left:431px">Services</a>
  <a href="#" style="left:524px">Portfolio</a>
  <a href="#" style="left:614px">Careers</a>
  <a href="#" style="left:699px">Gallery</a>
  <a href="#" style="left:778px">Legal</a>
</nav>
<div class="abs url center">www.calderaquatics.com</div>

</body>
</html>
```